Haulage company, lets use ruby red white and some 3rd color for web design. and Alder Croft Transport logo

Target Market(s)

Transport industry

Industry/Entity Type

transport

Number of Pages Required

2 page

Requirements
Must have
• Logo

```html
<!DOCTYPE html>
<html lang="en">
<head>
<meta charset="UTF-8">
<title>Alder Croft Transport</title>
<link rel="stylesheet" href="https://fonts.googleapis.com/css2?family=Montserrat:ital,wght@0,400;0,500;0,600;0,700;0,800;1,800&family=Fraunces:wght@600&display=swap">
<style>
:root{
  --ruby:#a30c0c;
  --paper:#f5f3f1;
  --ink:#3a2a22;
  --rule:#5a4a42;
  --sand:#d4ccc5;
  --card:#ffffff;
  --umber:#7b5a45;
}
*{margin:0;padding:0;box-sizing:border-box}
html,body{width:1200px;height:3000px;overflow:hidden;background:var(--paper)}
body{position:relative;font-family:"Montserrat",sans-serif;color:var(--ink)}
.abs{position:absolute}
.brand{position:absolute;display:flex;align-items:center;gap:10px;font-family:"Montserrat",sans-serif;font-weight:800;font-size:26px;line-height:28px;color:var(--ink);text-transform:uppercase;letter-spacing:.5px}
.brand-dot{width:30px;height:30px;border-radius:50%;background:var(--ruby);flex:none}
.rule{position:absolute;height:1px;background:var(--rule)}
.nav a{position:absolute;top:89px;font-size:15px;font-weight:500;color:var(--ink);text-decoration:none;letter-spacing:.5px}
.nav a.active{color:var(--ruby);font-weight:700;font-size:20px;top:86px;letter-spacing:1px}
.photo{position:absolute}
.hero-title{position:absolute;left:103px;top:234px;width:320px;font-family:"Fraunces",serif;font-weight:600;font-size:29px;line-height:40px;color:#fff}
.intro{position:absolute;left:91px;top:504px;width:408px;font-size:14px;line-height:19px;text-align:justify}
.pill{position:absolute;display:flex;align-items:center;justify-content:center;background:var(--ruby);color:#fff;font-weight:700;border-radius:999px;letter-spacing:1px}
.svc-title{position:absolute;font-size:33px;font-weight:600;color:var(--ruby)}
.svc-text{position:absolute;font-size:20px;line-height:27px;text-align:justify;letter-spacing:.3px}
.gallery-title{position:absolute;left:0;width:1220px;top:1664px;text-align:center;font-size:45px;font-weight:800;font-style:italic;color:var(--ink)}
.gallery-text{position:absolute;left:270px;width:680px;top:1722px;text-align:center;font-size:14px;line-height:19px}
.card{position:absolute;top:1815px;height:360px;background:var(--card)}
.cart{position:absolute;width:141px;height:24px;background:var(--sand);color:var(--ink);font-size:12px;font-weight:700;display:flex;align-items:center;justify-content:center;letter-spacing:.5px}
.contact-title{position:absolute;left:110px;top:2475px;font-size:42px;font-weight:600}
.field{position:absolute;left:663px;width:441px;background:var(--ruby);color:#fff;font-size:12px;font-weight:700;padding:10px;letter-spacing:.3px}
.footer{position:absolute;left:0;width:1230px;top:2954px;text-align:center;font-size:15px;font-weight:600;letter-spacing:.5px}
</style>
</head>
<body>

<header>
  <div class="brand" style="left:30px;top:52px">Alder<br>Croft<span class="brand-dot"></span></div>
  <nav class="nav">
    <a class="active" style="left:564px">HOME</a>
    <a style="left:676px">ABOUT</a>
    <a style="left:786px">SERVICES</a>
    <a style="left:897px">SOLUTIONS</a>
    <a style="left:1019px">CONTACT</a>
  </nav>
  <div class="rule" style="left:75px;top:136px;width:1049px"></div>
</header>

<section class="hero">
  <div class="photo" role="img" aria-label="Two refrigerated lorries driving along a coastal road under a cloudy sky" style="left:86px;top:150px;width:1028px;height:321px;background:linear-gradient(180deg,#8fb0d4 0%,#c9d6e2 30%,#4c6f8f 55%,#7d7f80 75%,#4a4d45 100%)"></div>
  <h1 class="hero-title">Delivering Reliable Haulage Services On Time</h1>
  <p class="intro">Welcome to Alder Croft Transport, your trusted partner for all your haulage needs. With our fleet of reliable vehicles and experienced drivers, we ensure timely and efficient delivery of your goods.</p>
  <div class="pill" style="left:87px;top:617px;width:207px;height:41px;font-size:21px">LEARN MORE</div>
  <div class="photo" role="img" aria-label="Two white and red lorry cabs parked on a yard" style="left:536px;top:490px;width:179px;height:181px;background:linear-gradient(180deg,#b9c4cc 0%,#dfe3e4 45%,#a7a9a5 100%)"></div>
  <div class="photo" role="img" aria-label="Lorries parked at night under floodlights" style="left:732px;top:492px;width:184px;height:184px;background:linear-gradient(180deg,#1e2426 0%,#4a4a45 55%,#6a6158 100%)"></div>
  <div class="photo" role="img" aria-label="Red and white lorry cab at sunset" style="left:930px;top:490px;width:183px;height:185px;background:linear-gradient(180deg,#3e73c4 0%,#7fa2d6 50%,#5a5d60 100%)"></div>
  <div class="rule" style="left:459px;top:732px;width:662px"></div>
  <div class="rule" style="left:459px;top:740px;width:662px"></div>
</section>

<section class="services">
  <div class="brand" style="left:69px;top:802px">Alder<br>Croft<span class="brand-dot"></span></div>
  <div class="rule" style="left:75px;top:885px;width:1049px"></div>
  <div class="photo" role="img" aria-label="White lorry with flatbed trailer loaded with steel in front of trees" style="left:75px;top:920px;width:467px;height:259px;border-radius:6px;background:linear-gradient(180deg,#2f4a22 0%,#4f6e35 45%,#8d8a80 75%,#6b6a62 100%)"></div>
  <h2 class="svc-title" style="left:598px;top:955px">Logistics Services</h2>
  <p class="svc-text" style="left:598px;top:1020px;width:524px">Our logistics services cover a wide range of transportation needs, from local deliveries to international shipments.</p>
  <div class="pill" style="left:958px;top:1114px;width:163px;height:32px;font-size:15px">READ MORE</div>

  <h2 class="svc-title" style="left:86px;top:1210px">Custom Solutions</h2>
  <p class="svc-text" style="left:86px;top:1285px;width:524px">We understand that every business has unique logistics requirements. That's why we offer custom solutions tailored to your specific needs.</p>
  <div class="pill" style="left:447px;top:1383px;width:163px;height:31px;font-size:15px">READ MORE</div>
  <div class="photo" role="img" aria-label="Two lorries on a coastal road beside the sea" style="left:665px;top:1187px;width:459px;height:268px;background:linear-gradient(180deg,#8fb0d4 0%,#c9d6e2 25%,#4c6f8f 45%,#7d7f80 70%,#56604a 100%)"></div>
</section>

<section class="gallery">
  <div class="brand" style="left:30px;top:1554px">Alder<br>Croft<span class="brand-dot"></span></div>
  <div class="rule" style="left:75px;top:1636px;width:1049px"></div>
  <h2 class="gallery-title">OUR GALLERY</h2>
  <p class="gallery-text">At Alder Croft Transport, we offer a comprehensive range of logistics services, including freight transport and custom solutions. With our expertise and dedication, we ensure that your goods are delivered safely and on time.</p>
  <div class="rule" style="left:115px;top:1803px;width:970px"></div>

  <svg class="abs" style="left:65px;top:1957px" width="28" height="50" viewBox="0 0 28 50" aria-hidden="true"><path d="M27 0 L0 25 L27 50 L20 25 Z" fill="var(--umber)"/></svg>
  <svg class="abs" style="left:1109px;top:1957px" width="28" height="50" viewBox="0 0 28 50" aria-hidden="true"><path d="M1 0 L28 25 L1 50 L8 25 Z" fill="var(--umber)"/></svg>

  <div class="card" style="left:101px;width:242px"></div>
  <div class="photo" role="img" aria-label="Lorries on a coastal road under a bright sky" style="left:106px;top:1823px;width:234px;height:230px;background:linear-gradient(180deg,#3f78c8 0%,#c8d4e0 40%,#6b7a86 65%,#5a5f55 100%)"></div>
  <div class="cart" style="left:157px;top:2139px">ADD TO CART</div>

  <div class="card" style="left:353px;width:241px"></div>
  <div class="photo" role="img" aria-label="Red and white lorry cab at dusk" style="left:359px;top:1823px;width:229px;height:230px;background:linear-gradient(180deg,#3d6fc0 0%,#c9a08a 50%,#4d4f52 100%)"></div>
  <div class="cart" style="left:408px;top:2090px">ADD TO CART</div>

  <div class="card" style="left:605px;width:241px"></div>
  <div class="photo" role="img" aria-label="Two lorry cabs parked on a yard" style="left:609px;top:1823px;width:234px;height:230px;background:linear-gradient(180deg,#b9c4cc 0%,#dfe3e4 45%,#a7a9a5 100%)"></div>
  <div class="cart" style="left:659px;top:2139px">ADD TO CART</div>

  <div class="card" style="left:855px;width:242px"></div>
  <div class="photo" role="img" aria-label="White lorry cab with flatbed trailer in front of trees" style="left:864px;top:1823px;width:232px;height:230px;background:linear-gradient(180deg,#2f4a22 0%,#6a7f55 45%,#e4e4e0 70%,#a6a59e 100%)"></div>
  <div class="cart" style="left:911px;top:2091px">ADD TO CART</div>
</section>

<section class="contact">
  <div class="brand" style="left:30px;top:2304px">Alder<br>Croft<span class="brand-dot"></span></div>
  <div class="rule" style="left:75px;top:2386px;width:1049px"></div>
  <h2 class="contact-title">Contact</h2>
  <div class="abs" style="left:110px;top:2670px;font-size:18px;font-weight:600">E-mail:</div>
  <div class="abs" style="left:110px;top:2699px;font-size:16px;font-weight:500">www.aldercroft-haulage.com</div>

  <div class="field" style="top:2484px;height:50px;padding-top:18px">NAME</div>
  <div class="field" style="top:2548px;height:49px;padding-top:18px">E-MAIL</div>
  <div class="field" style="top:2611px;height:50px;padding-top:18px">SUBJECT</div>
  <div class="field" style="top:2675px;height:164px">MESSAGE</div>
  <div class="pill" style="left:935px;top:2858px;width:169px;height:32px;font-size:15px">SUBMIT</div>
</section>

<footer class="footer">© 2024 ALDER CROFT TRANSPORT. ALL RIGHTS RESERVED.</footer>

</body>
</html>
```